Communication Skill: TECH Support

I need a Design for a skill I teach to youth. That's why the title TECH Support. TECH stands for Thoughts, Emotions, Concerns, Hopes & Desires. Under each word are some examples that are meant to help people discuss certain things. I tried to create something myself but want something much more creative and dynamic. I have attached what I designed because it has the information I need in the design. Want it to have a techie look to it.

```html
<!DOCTYPE html>
<html lang="en">
<head>
<meta charset="utf-8">
<title>TECH Support – Communication Skill</title>
<link rel="stylesheet" href="https://fonts.googleapis.com/css2?family=Roboto+Condensed:ital,wght@1,700&family=Tinos:ital@1&display=swap">
<style>
  :root {
    --sky-deep: #00b9ea;
    --sky: #5fcdf0;
    --mint: #bfe4d8;
    --cream: #fdf6bd;
    --thoughts: #f7a521;
    --emotions: #5f5ba7;
    --concerns: #b44a99;
    --hopes: #00aadf;
    --ring: #ffffff;
    --ink: #0b0b0b;
  }
  html, body {
    margin: 0;
    padding: 0;
    width: 1200px;
    height: 848px;
    overflow: hidden;
    background: var(--cream);
  }
  .poster {
    position: relative;
    width: 1200px;
    height: 848px;
  }
  .poster svg {
    display: block;
  }
  .title {
    font-family: "Tinos", "Times New Roman", serif;
    font-style: italic;
    font-size: 76px;
    fill: var(--ink);
  }
  .bubble-heading {
    font-family: "Roboto Condensed", "Arial Narrow", sans-serif;
    font-style: italic;
    font-weight: 700;
    font-size: 42px;
    fill: #fff;
    text-anchor: middle;
  }
  .bubble-line {
    font-family: "Roboto Condensed", "Arial Narrow", sans-serif;
    font-style: italic;
    font-weight: 700;
    font-size: 25px;
    fill: #fff;
    text-anchor: middle;
  }
  .heading-rule {
    stroke: #fff;
    stroke-width: 1.6;
    stroke-dasharray: 1.6 2.4;
  }
</style>
</head>
<body>
<main class="poster">
  <svg width="1200" height="848" viewBox="0 0 1200 848" aria-label="TECH Support communication skill poster">
    <defs>
      <linearGradient id="bg-fade" x1="0" y1="0" x2="0.25" y2="1">
        <stop offset="0" stop-color="var(--sky)"/>
        <stop offset="0.55" stop-color="var(--mint)"/>
        <stop offset="1" stop-color="var(--cream)"/>
      </linearGradient>
      <linearGradient id="corner-glow" x1="0" y1="0" x2="1" y2="1">
        <stop offset="0" stop-color="var(--sky-deep)"/>
        <stop offset="0.6" stop-color="#a9dde6" stop-opacity="0.8"/>
        <stop offset="1" stop-color="#f4f4dc" stop-opacity="0.9"/>
      </linearGradient>
      <linearGradient id="edge-sweep" x1="1" y1="0.4" x2="0.6" y2="1">
        <stop offset="0" stop-color="#73d1ef"/>
        <stop offset="1" stop-color="#eef6e6"/>
      </linearGradient>
    </defs>

    <!-- background -->
    <rect class="backdrop" width="1200" height="848" fill="url(#bg-fade)"/>
    <path class="backdrop-sweep" d="M0 0 H440 C400 200 220 400 0 515 Z" fill="url(#corner-glow)"/>
    <path class="backdrop-edge" d="M1200 525 C1070 610 980 720 950 848 H1200 Z" fill="url(#edge-sweep)"/>

    <!-- title -->
    <text class="title" x="116" y="137">Tech</text>
    <text class="title" x="60" y="209">Support</text>

    <!-- Thoughts -->
    <g class="bubble bubble-thoughts">
      <circle cx="566" cy="263" r="197" fill="var(--ring)"/>
      <circle cx="557" cy="263" r="188" fill="var(--thoughts)"/>
      <text class="bubble-heading" x="557" y="224">Thoughts</text>
      <line class="heading-rule" x1="464" y1="238" x2="650" y2="238"/>
      <text class="bubble-line" x="557" y="270">It seems…&#160;&#160;&#160; I wonder…</text>
      <text class="bubble-line" x="556" y="307">It’s my opinion…&#160;&#160; I believe…</text>
    </g>

    <!-- Emotions -->
    <g class="bubble bubble-emotions">
      <circle cx="974" cy="263" r="197" fill="var(--ring)"/>
      <circle cx="965" cy="263" r="188" fill="var(--emotions)"/>
      <text class="bubble-heading" x="965" y="186">Emotions</text>
      <line class="heading-rule" x1="877" y1="194" x2="1060" y2="194"/>
      <text class="bubble-line" x="856" y="226">I’m…</text>
      <text class="bubble-line" x="949" y="226">hopeful</text>
      <text class="bubble-line" x="1057" y="226">worried</text>
      <text class="bubble-line" x="847" y="259">sad</text>
      <text class="bubble-line" x="923" y="259">afraid</text>
      <text class="bubble-line" x="1004" y="259">mad</text>
      <text class="bubble-line" x="1077" y="259">glad</text>
      <text class="bubble-line" x="843" y="291">happy</text>
      <text class="bubble-line" x="951" y="291">confident</text>
      <text class="bubble-line" x="1073" y="291">insecure</text>
      <text class="bubble-line" x="840" y="324">lonely</text>
      <text class="bubble-line" x="946" y="324">bothered</text>
      <text class="bubble-line" x="1069" y="324">uncertain</text>
    </g>

    <!-- Concerns -->
    <g class="bubble bubble-concerns">
      <circle cx="367" cy="629" r="197" fill="var(--ring)"/>
      <circle cx="358" cy="629" r="188" fill="var(--concerns)"/>
      <text class="bubble-heading" x="358" y="557">Concerns</text>
      <line class="heading-rule" x1="267" y1="566" x2="450" y2="566"/>
      <text class="bubble-line" x="357" y="603">I worry about…</text>
      <text class="bubble-line" x="357" y="640">I’m afraid that…</text>
      <text class="bubble-line" x="357" y="677">I’m nervous because…</text>
      <text class="bubble-line" x="357" y="714">It bothers me that…</text>
    </g>

    <!-- Hopes -->
    <g class="bubble bubble-hopes">
      <circle cx="774" cy="629" r="197" fill="var(--ring)"/>
      <circle cx="765" cy="629" r="188" fill="var(--hopes)"/>
      <text class="bubble-heading" x="765" y="553">Hopes</text>
      <line class="heading-rule" x1="687" y1="566" x2="838" y2="566"/>
      <text class="bubble-line" x="764" y="599">I hope…&#160;&#160; I wish…</text>
      <text class="bubble-line" x="764" y="636">It’s my desire…</text>
      <text class="bubble-line" x="764" y="673">I’d like to see…</text>
      <text class="bubble-line" x="764" y="710">I want…&#160;&#160; I need…</text>
    </g>
  </svg>
</main>
</body>
</html>
```